Design a menu for a Pizza company

I need help designing a color menu for a pizza company. It will be a 9x16" trifold menu (3-panel). I would like to include some photos of pizza, salads, subs, sandwiches, drinks, etc. (no clipart). Attached is an example of an existing menu. I need to make the menu full color. We would like to modernize this menu with full color photos like the attached sample menu. The final files should have editable files so I can edit prices and menu items as needed. I prefer CorelDraw graphics software.

Target Market(s)

General public.

Industry/Entity Type

Restaurant

Font styles to use
Sans Serif

Colors
ec1f27
fffefc
9bcb3b

Requirements
Must have
• Must have photos and editable fonts. I will need to be able to edit the contents of the menu after you provide me with the final files.
Nice to have
• It would be nice to have this menu created in CorelDraw X7 or X8.
Should not have
• Should not have clip art or low resolution photos.

```html
<!DOCTYPE html>
<html lang="en">
<head>
<meta charset="utf-8">
<title>Quarzino Pizza – Trifold Menu</title>
<link href="https://fonts.googleapis.com/css2?family=Roboto+Condensed:ital,wght@0,400;0,700;1,400;1,700&family=Roboto+Slab:wght@400;700&display=swap" rel="stylesheet">
<style>
  :root{
    --red:#c0000d;
    --red-deep:#8a0008;
    --red-text:#b0101a;
    --green:#8cc43a;
    --paper:#fffefc;
    --backdrop:#8f9196;
    --white:#ffffff;
  }
  *{box-sizing:border-box;margin:0;padding:0}
  html,body{width:1200px;height:984px;overflow:hidden}
  body{background:var(--backdrop);font-family:"Roboto Condensed",Arial,sans-serif;position:relative}
  .menu{position:absolute;left:30px;top:171px;width:1140px;height:641px;box-shadow:0 14px 40px rgba(0,0,0,.35);overflow:hidden}
  .panel{position:absolute;top:0;height:641px;width:380px}
  .panel--inside-left{left:0;background:var(--paper);padding:16px 26px;color:var(--red-text);font-size:11.5px}
  .backdrop-shapes{position:absolute;left:380px;top:0;width:760px;height:641px}

  .section-title{font-family:"Roboto Condensed",sans-serif;font-style:italic;font-weight:700;color:var(--green);font-size:19px;text-align:center;margin:8px 0 2px;letter-spacing:.3px}
  .section-title::before,.section-title::after{content:"~";margin:0 8px;font-weight:400}
  .section-note{text-align:center;font-style:italic;font-size:10.5px;line-height:12px;margin-bottom:4px}
  .item{display:flex;align-items:baseline;line-height:13.5px}
  .item .name{white-space:nowrap}
  .item .dots{flex:1;border-bottom:1px dotted currentColor;margin:0 4px;transform:translateY(-3px)}
  .item .price{white-space:nowrap}
  .notice{text-align:center;font-style:italic;font-size:10.5px;line-height:12.5px;margin:8px 0 2px}

  .size-table{width:100%;border-collapse:collapse;font-size:11px}
  .size-table th{font-weight:400;font-style:italic;text-align:right;padding:0 2px}
  .size-table td{text-align:right;line-height:13px;padding:0 2px}
  .size-table td.drink{text-align:left}

  .panel--inside-middle{left:380px;color:var(--white);padding:36px 26px 0;font-size:11.5px}
  .panel--inside-middle .section-title{font-size:18px;margin-top:4px}
  .sub-title{text-align:center;font-family:"Roboto Slab",serif;font-size:15px;margin:6px 0 2px}
  .panel--inside-middle .size-table{color:var(--white)}

  .panel--cover{left:760px;color:var(--white);padding:44px 30px 0}
  .brand{display:flex;align-items:center;justify-content:center;gap:10px;margin:20px 0 70px;white-space:nowrap}
  .brand-mark{width:14px;height:14px;background:var(--white);flex:none}
  .brand-name{font-family:"Roboto Slab",serif;font-weight:700;font-size:24px;letter-spacing:1px;text-transform:uppercase}
  .open-days{font-family:"Roboto Slab",serif;font-weight:700;font-size:19px;text-align:center;margin-bottom:12px;white-space:nowrap}
  .open-days::before,.open-days::after{content:"~";font-weight:400;margin:0 10px}
  .hours{display:grid;grid-template-columns:1fr auto;row-gap:2px;font-family:"Roboto Slab",serif;font-size:13px;margin:0 6px 14px}
  .hours dd{text-align:right}
  .payment{font-family:"Roboto Slab",serif;font-size:15px;text-align:center}

  .tagline{position:absolute;left:380px;top:578px;width:520px;text-align:center;font-family:"Roboto Slab",serif;font-weight:700;color:var(--red);font-size:26px;letter-spacing:.5px;white-space:nowrap}
  .tagline::before,.tagline::after{content:"~";font-weight:400;margin:0 14px;font-size:22px}
</style>
</head>
<body>
<main class="menu">

  <section class="panel panel--inside-left">
    <h2 class="section-title">ITALIAN DINNERS</h2>
    <p class="section-note">Served on Garlic Bread &amp; Salad<br>Choice of Dressing:<br>Ranch, French, Italian, Blue Cheese, Thousand Island</p>
    <div class="item"><span class="name">Spaghetti w/ Meat Sauce</span><span class="dots"></span><span class="price">3.99</span></div>
    <div class="item"><span class="name">Spaghetti w/ Meatballs</span><span class="dots"></span><span class="price">9.99</span></div>
    <div class="item"><span class="name">Veal Parmigiana w/ Spaghetti</span><span class="dots"></span><span class="price">9.99</span></div>
    <div class="item"><span class="name">Chicken Parmigiana w/ Spaghetti</span><span class="dots"></span><span class="price">9.99</span></div>
    <div class="item"><span class="name">Eggplant Parmigiana w/ Spaghetti</span><span class="dots"></span><span class="price">9.99</span></div>
    <div class="item"><span class="name">Baked Lasagna</span><span class="dots"></span><span class="price">9.99</span></div>
    <div class="item"><span class="name">Ravioli w/ Meat Sauce</span><span class="dots"></span><span class="price">9.99</span></div>

    <h2 class="section-title">SEAFOOD DINNERS</h2>
    <p class="section-note">Served on Garlic Bread, French Fries &amp; Salad<br>Choice of Dressing:<br>Ranch, French, Italian, Blue Cheese, Thousand Island</p>
    <div class="item"><span class="name">Shrimp Basket</span><span class="dots"></span><span class="price">8.99</span></div>
    <div class="item"><span class="name">Crab Cake</span><span class="dots"></span><span class="price">10.99</span></div>
    <div class="item"><span class="name">Fish Filet</span><span class="dots"></span><span class="price">10.99</span></div>

    <h2 class="section-title">CHILDREN'S MENU</h2>
    <div class="item"><span class="name">Chicken Tenders w/ French Fries</span><span class="dots"></span><span class="price">5.99</span></div>
    <div class="item"><span class="name">Spaghetti w/ Meat Sauce</span><span class="dots"></span><span class="price">5.99</span></div>
    <div class="item"><span class="name">Ravioli w/ Meat Sauce</span><span class="dots"></span><span class="price">5.99</span></div>
    <div class="item"><span class="name">Shrimp w/ French Fries</span><span class="dots"></span><span class="price">5.99</span></div>
    <div class="item"><span class="name">Cheeseburger w/ French Fries &amp; small Beverage</span><span class="dots"></span><span class="price">5.99</span></div>
    <p class="notice">"These items are cooked to order.<br>Consuming raw or undercooked meats may increase<br>you risk of foodborne illness."</p>

    <h2 class="section-title">SODA</h2>
    <table class="size-table">
      <tr><th style="text-align:left">Pitcher</th><th></th><th></th><th></th><td>3.99</td></tr>
      <tr><th></th><th>12 oz.</th><th>16 oz.</th><th>24 oz.</th><th>32 oz.</th></tr>
      <tr><td class="drink">Cola</td><td>.99</td><td>1.30</td><td>1.69</td><td>1.99</td></tr>
      <tr><td class="drink">Lemon-Lime</td><td>.99</td><td>1.30</td><td>1.69</td><td>1.99</td></tr>
      <tr><td class="drink">Root Beer</td><td>.99</td><td>1.30</td><td>1.69</td><td>1.99</td></tr>
      <tr><td class="drink">Diet Cola</td><td>.99</td><td>1.30</td><td>1.69</td><td>1.99</td></tr>
    </table>
  </section>

  <svg class="backdrop-shapes" viewBox="0 0 760 641">
    <defs>
      <linearGradient id="deepBand" x1="0" y1="0" x2="1" y2="1">
        <stop offset="0" stop-color="#9a000a"/><stop offset="1" stop-color="#6e0006"/>
      </linearGradient>
      <linearGradient id="chefPhoto" x1="0" y1="0" x2="1" y2="1">
        <stop offset="0" stop-color="#d99a55"/><stop offset=".5" stop-color="#e8d9c8"/><stop offset="1" stop-color="#c9853f"/>
      </linearGradient>
      <linearGradient id="saladPhoto" x1="0" y1="0" x2="1" y2="1">
        <stop offset="0" stop-color="#d8d3c8"/><stop offset=".45" stop-color="#7fa23a"/><stop offset="1" stop-color="#e2603a"/>
      </linearGradient>
      <linearGradient id="pizzaPhoto" x1="0" y1="0" x2="1" y2="1">
        <stop offset="0" stop-color="#6f8a3a"/><stop offset=".5" stop-color="#e8b46a"/><stop offset="1" stop-color="#cc3b2c"/>
      </linearGradient>
    </defs>
    <rect x="0" y="0" width="760" height="641" fill="var(--red)"/>
    <path d="M0 0 H380 V388 Q190 396 0 404 Z" fill="url(#deepBand)"/>
    <polygon role="img" aria-label="Photo of a chef figure holding a pizza" points="0,410 380,394 380,560 300,560 0,430" fill="url(#chefPhoto)"/>
    <polygon points="380,394 430,394 760,560 380,560" fill="var(--white)"/>
    <polygon role="img" aria-label="Photo of a fresh salad with broccoli and peppers" points="380,402 412,402 712,560 380,560" fill="url(#saladPhoto)"/>
    <polygon points="560,428 760,428 760,434 572,434" fill="var(--white)"/>
    <polygon role="img" aria-label="Photo of a pizza topped with tomato and olives" points="574,438 760,438 760,540 740,548" fill="url(#pizzaPhoto)"/>
    <rect x="0" y="560" width="760" height="81" fill="var(--white)"/>
    <polygon points="620,560 760,560 760,632" fill="var(--red-deep)"/>
  </svg>

  <section class="panel panel--inside-middle">
    <h2 class="section-title">BEVERAGES</h2>
    <table class="size-table">
      <tr><th></th><th>16 oz.</th><th>24 oz.</th><th>32 oz.</th></tr>
      <tr><td class="drink">ICED TEA</td><td>1.30</td><td>1.69</td><td>1.99</td></tr>
    </table>
    <h2 class="section-title">BEER</h2>
    <p class="sub-title">DRAFT</p>
    <div class="item"><span class="name">32 OZ. PITCHER</span><span class="dots"></span><span class="price">6.99</span></div>
    <div class="item"><span class="name">60 OZ. PITCHER</span><span class="dots"></span><span class="price">10.99</span></div>
    <div class="item"><span class="name">RED BARN LAGER</span><span class="dots"></span><span class="price">2.60</span></div>
    <p class="sub-title">BOTTLES</p>
    <div class="item"><span class="name">RED BARN LAGER</span><span class="dots"></span><span class="price">3.25</span></div>
    <div class="item"><span class="name">MILLBROOK</span><span class="dots"></span><span class="price">3.25</span></div>
    <div class="item"><span class="name">MILLBROOK LIGHT</span><span class="dots"></span><span class="price">3.25</span></div>
    <div class="item"><span class="name">RIDGELINE</span><span class="dots"></span><span class="price">3.25</span></div>
    <div class="item"><span class="name">RIDGELINE LIGHT</span><span class="dots"></span><span class="price">3.25</span></div>
    <p class="sub-title">IMPORTED BOTTLES</p>
    <div class="item"><span class="name">HARBOR GOLD</span><span class="dots"></span><span class="price">3.75</span></div>
    <div class="item"><span class="name">COSTA CLARA</span><span class="dots"></span><span class="price">3.75</span></div>
  </section>

  <section class="panel panel--cover">
    <div class="brand"><span class="brand-mark"></span><span class="brand-name">Quarzino Pizza</span></div>
    <h2 class="open-days">OPEN 7 DAYS A WEEK</h2>
    <dl class="hours">
      <dt>MONDAY-THURSDAY</dt><dd>10.30 A.M. - 9.30 P.M.</dd>
      <dt>FRIDAY-SATURDAY</dt><dd>10.30 A.M. - 10.00 P.M.</dd>
      <dt>SUNDAY</dt><dd>12 NOON - 8.00 P.M.</dd>
    </dl>
    <p class="payment">Major Credit Cards Accepted</p>
  </section>

  <p class="tagline">DINE-IN &amp; CARRY OUT</p>
</main>
</body>
</html>
```